Process Engineering/Construction Firm wants a OneSheet targeting craft brewers in Texas

We need a OneSheet (standard letter size) that we can share with craft brewers in our state, that explains what we can do for them. This will be shared primarily via email and online. We would like to see this be fun and modern flyer while still maintaining our professional vibe. More info and logos are uploaded - please review. Also, this project could lead to more branded documents from OneSheets to letterhead. We have our website and our logo(s) and really not much else that is consistent. There is certainly opportunity to work long-term.
Updates

Please note that the website listed on the flyer should read www.halvernworksadvisory.com. It will NOT follow the same domain name as the email address. And also, please DO NOT send me anything through the sales@hwaadvisoryllc.com email address at this time. I am trying to find a brewery-specific photo to use and will upload once found. I will be uploading shortly another logo of an affiliate organization we belong to - the Lone Kettle Brewing Alliance that I would like to see included on the flyer with the words, "A proud member of the Lone Kettle Brewing Alliance' OR just 'Proud Member.'

Target Market(s)

Craft brewery owners in Texas

Industry/Entity Type

Engineering

Font styles to use
Sans Serif

Requirements
Must have
• We need our point of contact to list the website as well as this email: sales@hwaadvisoryllc.com
• Maroon CMYK is: 32, 100, 82, 30
• We want these Brewery Specific service points included:
• • Brewhouse automation
• • Glycol systems
• • Complete line design and install
• • Packaging solutions
• • Epoxy & urethane flooring
• • New construction
• • Network of industry professionals
Nice to have
• Trendy and modern look to correlate with current craft beer logos and design trends

```html
<!DOCTYPE html>
<html lang="en">
<head>
<meta charset="utf-8">
<title>Halvern Works Advisory – Brewery Services One-Sheet</title>
<link rel="stylesheet" href="https://fonts.googleapis.com/css2?family=Open+Sans:wght@400;700;800&family=Fira+Sans+Extra+Condensed:wght@600&display=swap">
<style>
  :root {
    --maroon: #861f32;
    --maroon-deep: #6e1426;
    --ink: #1b1b1b;
    --white: #ffffff;
    --navy: #1f2f5c;
    --dark: #2c2d30;
    --stage: #d9d9d9;
  }
  * { box-sizing: border-box; margin: 0; padding: 0; }
  html, body { width: 1200px; height: 1200px; overflow: hidden; background: var(--stage); }
  .sheet {
    position: absolute; left: 160px; top: 30px; width: 881px; height: 1140px;
    background: var(--dark); overflow: hidden;
    font-family: "Open Sans", Arial, sans-serif; color: var(--white);
  }
  .hero-photo {
    position: absolute; left: 0; top: 0; width: 881px; height: 524px;
    background: radial-gradient(ellipse at 50% 70%, #d98a2c 0%, #8c3f14 35%, #4a1c0d 70%, #2a120a 100%);
  }
  .plant-photo {
    position: absolute; left: 0; top: 530px; width: 881px; height: 550px;
    background: linear-gradient(180deg, #3a3b3f 0%, #2e2f32 50%, #36373a 100%);
  }
  .shapes { position: absolute; left: 0; top: 0; }
  .brand { position: absolute; left: 70px; top: 72px; width: 360px; text-align: center; }
  .brand-name { font-weight: 800; font-size: 27px; color: var(--ink); letter-spacing: -0.3px; }
  .brand-tag { font-weight: 700; font-size: 12.5px; color: var(--ink); letter-spacing: 0.6px; margin-top: 2px; }
  .member-badge { position: absolute; left: 649px; top: 29px; width: 200px; height: 200px; }
  .pitch { position: absolute; left: 0; top: 573px; width: 881px; text-align: center; }
  .pitch-question { font-size: 19.5px; }
  .pitch-line { font-weight: 800; font-size: 28px; margin-top: 2px; }
  .services-title {
    position: absolute; left: 279px; top: 657px; width: 323px; height: 52px;
    background: var(--maroon); border-bottom: 3px solid var(--white);
    font-weight: 700; font-size: 42px; line-height: 48px; text-align: center;
  }
  .service { position: absolute; width: 200px; margin-left: -100px; text-align: center; }
  .service-icon {
    display: block; margin: 0 auto; width: 92px; height: 92px; border-radius: 50%;
    background: var(--white); border: 3px solid var(--maroon); box-shadow: 0 0 0 3px var(--white);
  }
  .service-icon svg { width: 86px; height: 86px; }
  .service-label {
    font-family: "Fira Sans Extra Condensed", "Arial Narrow", sans-serif; font-weight: 600;
    font-size: 19.5px; line-height: 24px; margin-top: 17px; text-transform: uppercase;
  }
  .footer {
    position: absolute; left: 0; top: 1080px; width: 881px; height: 60px;
    background: var(--maroon); border-top: 3px solid var(--white);
    display: flex; justify-content: center; align-items: center; gap: 40px; font-size: 20.5px;
  }
  .contact { display: flex; align-items: center; gap: 8px; }
  .contact-dot { width: 20px; height: 20px; border-radius: 50%; background: var(--white); display: flex; align-items: center; justify-content: center; }
</style>
</head>
<body>
<main class="sheet">
  <div class="hero-photo" role="img" aria-label="Flight of five craft beers, pale to dark, on a wooden paddle in a taproom"></div>
  <div class="plant-photo" role="img" aria-label="Faded view of a brewery packaging line with conveyors and tanks"></div>

  <svg class="shapes" width="881" height="1140" viewBox="0 0 881 1140" aria-hidden="true">
    <path d="M0,0 H612 C560,135 430,218 230,218 C130,218 50,206 0,190 Z" fill="var(--maroon)"/>
    <path d="M0,0 H590 C540,120 420,204 230,204 C130,204 50,194 0,178 Z" fill="var(--white)"/>
    <path d="M0,520 Q440,505 881,520 V532 Q440,517 0,532 Z" fill="var(--white)"/>
    <path d="M0,524 Q440,509 881,524 V540 Q440,524 0,540 Z" fill="var(--maroon)"/>
  </svg>

  <div class="brand">
    <div class="brand-name">Halvern Works Advisory</div>
    <div class="brand-tag">ENGINEERING - CONSTRUCTION</div>
  </div>

  <svg class="member-badge" viewBox="0 0 200 200" role="img" aria-label="Proud member of the Lone Kettle Brewing Alliance badge">
    <circle cx="100" cy="100" r="99" fill="var(--white)"/>
    <circle cx="100" cy="100" r="94" fill="var(--navy)"/>
    <circle cx="100" cy="100" r="64" fill="none" stroke="var(--white)" stroke-width="2"/>
  </svg>

  <section class="pitch">
    <p class="pitch-question">Have questions about expanding? Need guidance for new equipment?</p>
    <p class="pitch-line">Let HWA help you brew the best solutions.</p>
  </section>

  <h2 class="services-title">our services</h2>

  <div class="service" style="left:238px; top:741px;">
    <span class="service-icon"><svg viewBox="0 0 86 86" fill="none" stroke="var(--maroon)" stroke-width="2.5">
      <circle cx="43" cy="43" r="9"/><circle cx="43" cy="43" r="15" stroke-dasharray="5 4"/>
      <path d="M22 36 A22 22 0 0 1 60 28"/><path d="M64 50 A22 22 0 0 1 26 58"/>
      <path d="M60 22 V29 H53"/><path d="M26 64 V57 H33"/></svg></span>
    <p class="service-label">Brewhouse Automation</p>
  </div>
  <div class="service" style="left:440px; top:741px;">
    <span class="service-icon"><svg viewBox="0 0 86 86" fill="none" stroke="var(--maroon)" stroke-width="2.5">
      <rect x="36" y="20" width="7" height="16" rx="3"/><path d="M39 36 V46 H28 V54"/>
      <path d="M24 46 H46"/><rect x="50" y="36" width="10" height="30"/><path d="M34 62 V66"/></svg></span>
    <p class="service-label">Glycol Systems</p>
  </div>
  <div class="service" style="left:643px; top:741px;">
    <span class="service-icon"><svg viewBox="0 0 86 86" fill="none" stroke="var(--maroon)" stroke-width="2.5">
      <rect x="26" y="26" width="12" height="11"/><rect x="46" y="26" width="12" height="11"/>
      <rect x="18" y="41" width="50" height="12" rx="6"/>
      <circle cx="26" cy="47" r="2.5"/><circle cx="36" cy="47" r="2.5"/><circle cx="46" cy="47" r="2.5"/><circle cx="56" cy="47" r="2.5"/>
      <path d="M30 53 V60 M56 53 V60 M24 60 H62"/></svg></span>
    <p class="service-label">Complete Line Design<br>and Install</p>
  </div>

  <div class="service" style="left:136px; top:897px;">
    <span class="service-icon"><svg viewBox="0 0 86 86" fill="none" stroke="var(--maroon)" stroke-width="2.5">
      <path d="M28 22 V30 L25 35 V44 H33 V35 L30 30 V22Z"/><path d="M41 22 V30 L38 35 V44 H46 V35 L43 30 V22Z"/><path d="M54 22 V30 L51 35 V44 H59 V35 L56 30 V22Z"/>
      <rect x="20" y="44" width="44" height="20"/><path d="M20 54 H64 M30 58 H54"/></svg></span>
    <p class="service-label">Packaging Solutions</p>
  </div>
  <div class="service" style="left:339px; top:897px;">
    <span class="service-icon"><svg viewBox="0 0 86 86" fill="none" stroke="var(--maroon)" stroke-width="2.5">
      <path d="M43 18 C39 25 36 29 36 33 A7 7 0 0 0 50 33 C50 29 47 25 43 18Z"/>
      <path d="M16 46 H70"/><path d="M22 62 L30 48 M30 62 L38 48 M38 62 L46 48 M46 62 L54 48 M54 62 L62 48"/></svg></span>
    <p class="service-label">Epoxy &amp; Urethane<br>Flooring</p>
  </div>
  <div class="service" style="left:541px; top:897px;">
    <span class="service-icon"><svg viewBox="0 0 86 86" fill="none" stroke="var(--maroon)" stroke-width="2.5">
      <rect x="22" y="32" width="20" height="32"/><path d="M26 38 H30 M34 38 H38 M26 46 H30 M34 46 H38 M26 54 H30 M34 54 H38"/>
      <path d="M48 64 V24 L62 20 M48 28 L60 36 V46"/><circle cx="48" cy="24" r="3"/><rect x="56" y="46" width="8" height="18"/></svg></span>
    <p class="service-label">New Construction</p>
  </div>
  <div class="service" style="left:743px; top:897px;">
    <span class="service-icon"><svg viewBox="0 0 86 86" fill="none" stroke="var(--maroon)" stroke-width="2.5">
      <circle cx="43" cy="43" r="7"/><circle cx="43" cy="21" r="4"/><circle cx="43" cy="65" r="4"/>
      <circle cx="24" cy="32" r="4"/><circle cx="62" cy="32" r="4"/><circle cx="24" cy="54" r="4"/><circle cx="62" cy="54" r="4"/>
      <path d="M43 25 V36 M43 50 V61 M28 34 L37 40 M58 34 L49 40 M28 52 L37 46 M58 52 L49 46 M27 30 L40 22 M59 30 L46 22 M24 36 V50 M62 36 V50"/></svg></span>
    <p class="service-label">Network of Industry<br>Professionals</p>
  </div>

  <footer class="footer">
    <span class="contact"><span class="contact-dot"><svg width="13" height="10" viewBox="0 0 13 10" fill="none" stroke="var(--maroon)" stroke-width="1.5"><rect x="0.75" y="0.75" width="11.5" height="8.5"/><path d="M1 1 L6.5 5.5 L12 1"/></svg></span>sales@hwaadvisoryllc.com</span>
    <span class="contact"><span class="contact-dot"><svg width="14" height="14" viewBox="0 0 14 14" fill="none" stroke="var(--maroon)" stroke-width="1.2"><circle cx="7" cy="7" r="6"/><ellipse cx="7" cy="7" rx="2.6" ry="6"/><path d="M1 7 H13"/></svg></span>www.halvernworksadvisory.com</span>
  </footer>
</main>
</body>
</html>
```